Can Design for Fun, Growing Health Food Brand

We are launching a brand new product, electrolyte seltzer drinks. We want the design to be clean/simple and slightly modern while staying true to our brand identity. Must say "Mineral Hydration" as the product descriptor, sub headline is "Carbonated electrolyte beverage with sea moss and real fruit juice". First flavors will be Watermelon Mint and Mango.

Target Market(s)

Women ages 30-50 who are interested in health wellness/trends

Industry/Entity Type

Health & Wellness

Font styles to use
Sans Serif

Requirements
Must have
• Tall, skinny can, current Brightfen Kelp Logo, use aluminum on can as element in design.
Nice to have
• Be fun, clean and modern. Would like to see the label less busy than our gels.
Should not have
• Avoid putting flavor on bottom 1/5 of can. No gradient color changes. Do not want really detailed or realistic fruit image, prefer drawings or similar.

```html
<!DOCTYPE html>
<html lang="en">
<head>
<meta charset="utf-8">
<title>Brightfen Kelp – Mineral Hydration</title>
<link href="https://fonts.googleapis.com/css2?family=Barlow+Semi+Condensed:wght@500;600&family=Mulish:wght@500;700&display=swap" rel="stylesheet">
<style>
  :root {
    --ink: #143d33;
    --label: #f3f3f1;
    --aluminum: #c8cbcd;
    --aluminum-dark: #a9adb0;
    --mango: #e39a2c;
    --mango-band: #f4c36c;
    --mango-fruit: #f1b53a;
    --melon: #d9485f;
    --melon-band: #f0aeb3;
    --melon-fruit: #e8606c;
    --page: #ffffff;
  }
  * { box-sizing: border-box; margin: 0; padding: 0; }
  html, body { width: 1024px; height: 1200px; overflow: hidden; background: var(--page); }
  .range {
    position: relative; width: 1024px; height: 1200px;
    display: flex; justify-content: center; gap: 44px; padding-top: 100px;
  }
  .can {
    position: relative; width: 330px; height: 990px;
    background: var(--label); border-radius: 20px; overflow: hidden;
    color: var(--ink); text-align: center;
    font-family: "Mulish", sans-serif;
  }
  .can__rim {
    position: absolute; left: 0; right: 0; height: 26px; background: var(--aluminum);
  }
  .can__rim--top { top: 0; border-bottom: 3px solid var(--aluminum-dark); }
  .can__rim--bottom { bottom: 0; border-top: 3px solid var(--aluminum-dark); }
  .brand { position: absolute; top: 68px; left: 0; right: 0; }
  .brand__dot {
    width: 92px; height: 92px; margin: 0 auto;
    border: 5px solid var(--ink); border-radius: 50%;
  }
  .brand__name {
    margin-top: 16px;
    font-family: "Barlow Semi Condensed", sans-serif; font-weight: 500;
    font-size: 33px; letter-spacing: -0.5px; color: var(--ink);
  }
  .descriptor {
    position: absolute; top: 262px; left: 0; right: 0;
    font-family: "Barlow Semi Condensed", sans-serif; color: var(--ink);
  }
  .descriptor__main { display: block; font-weight: 600; font-size: 90px; line-height: 0.95; letter-spacing: 2px; }
  .descriptor__sub { display: block; font-weight: 500; font-size: 63px; line-height: 1.05; letter-spacing: 3px; }
  .divider { position: absolute; top: 440px; left: 122px; width: 86px; height: 2px; }
  .can--mango .divider { background: var(--mango); }
  .can--melon .divider { background: var(--melon); }
  .tagline {
    position: absolute; top: 462px; left: 0; right: 0;
    font-size: 13.5px; font-weight: 500; line-height: 1.6; color: var(--ink);
  }
  .band { position: absolute; left: 0; top: 540px; width: 330px; height: 450px; }
  .fruit {
    position: absolute; top: 548px; left: 80px; width: 200px; height: 160px;
    border-radius: 46% 54% 40% 60% / 55% 50% 50% 45%;
  }
  .can--mango .fruit { background: radial-gradient(circle at 40% 55%, #f7cf5a, var(--mango-fruit) 60%, #d9862a); }
  .can--melon .fruit { background: radial-gradient(circle at 45% 40%, #f07a80, var(--melon-fruit) 55%, #4f8a3a); }
  .flavor {
    position: absolute; top: 728px; left: 0; right: 0;
    font-family: "Barlow Semi Condensed", sans-serif; font-weight: 600;
    font-size: 31px; line-height: 1.1; letter-spacing: 2px;
  }
  .can--mango .flavor { top: 742px; color: var(--mango); }
  .can--melon .flavor { color: var(--melon); }
  .claims {
    position: absolute; top: 810px; left: 16px; right: 16px;
    display: flex; justify-content: space-between;
  }
  .claim { width: 98px; display: flex; flex-direction: column; align-items: center; }
  .claim__icon {
    width: 44px; height: 44px; border: 1.5px solid var(--ink); border-radius: 50%;
    display: flex; align-items: center; justify-content: center;
  }
  .claim__text {
    margin-top: 9px; font-size: 12px; font-weight: 700; line-height: 1.45;
    text-transform: uppercase; color: var(--ink);
  }
  .volume {
    position: absolute; top: 916px; left: 0; right: 0;
    font-family: "Barlow Semi Condensed", sans-serif; font-weight: 500; font-size: 23px;
  }
</style>
</head>
<body>
<main class="range">

  <section class="can can--mango">
    <div class="can__rim can__rim--top"></div>
    <div class="brand">
      <div class="brand__dot"></div>
      <p class="brand__name">BRIGHTFEN KELP</p>
    </div>
    <h1 class="descriptor">
      <span class="descriptor__main">MINERAL</span>
      <span class="descriptor__sub">HYDRATION</span>
    </h1>
    <div class="divider"></div>
    <p class="tagline">Carbonated electrolyte beverage<br>with sea moss and real fruit juice</p>
    <svg class="band" viewBox="0 0 330 450" aria-hidden="true">
      <path d="M0 18 C70 -4 140 10 180 30 C230 55 280 60 330 40 L330 450 L0 450 Z" fill="var(--mango-band)"/>
    </svg>
    <div class="fruit" role="img" aria-label="Mango with a cubed half and a leaf"></div>
    <p class="flavor">MANGO</p>
    <div class="claims">
      <div class="claim">
        <div class="claim__icon">
          <svg width="22" height="22" viewBox="0 0 24 24" aria-hidden="true"><path d="M12 20 C12 14 9 10 4 9 C4 15 7 19 12 20 Z M12 20 C12 14 15 10 20 9 C20 15 17 19 12 20 Z" fill="var(--ink)"/></svg>
        </div>
        <p class="claim__text">Plant<br>Based</p>
      </div>
      <div class="claim">
        <div class="claim__icon">
          <svg width="20" height="22" viewBox="0 0 20 24" aria-hidden="true"><path d="M10 2 C6 9 4 12 4 15.5 A6 6 0 0 0 16 15.5 C16 12 14 9 10 2 Z" fill="var(--ink)"/></svg>
        </div>
        <p class="claim__text">Low<br>Sugar</p>
      </div>
      <div class="claim">
        <div class="claim__icon">
          <svg width="22" height="22" viewBox="0 0 24 24" aria-hidden="true"><path d="M12 21 V6 M12 14 C9 12 8 9 8 6 M12 14 C15 12 16 9 16 6" stroke="var(--ink)" stroke-width="1.8" fill="none" stroke-linecap="round"/></svg>
        </div>
        <p class="claim__text">Made with<br>real sea moss</p>
      </div>
    </div>
    <p class="volume">12 FL OZ (355 mL)</p>
    <div class="can__rim can__rim--bottom"></div>
  </section>

  <section class="can can--melon">
    <div class="can__rim can__rim--top"></div>
    <div class="brand">
      <div class="brand__dot"></div>
      <p class="brand__name">BRIGHTFEN KELP</p>
    </div>
    <h1 class="descriptor">
      <span class="descriptor__main">MINERAL</span>
      <span class="descriptor__sub">HYDRATION</span>
    </h1>
    <div class="divider"></div>
    <p class="tagline">Carbonated electrolyte beverage<br>with sea moss and real fruit juice</p>
    <svg class="band" viewBox="0 0 330 450" aria-hidden="true">
      <path d="M0 22 C70 0 140 10 180 30 C230 55 280 60 330 40 L330 450 L0 450 Z" fill="var(--melon-band)"/>
    </svg>
    <div class="fruit" role="img" aria-label="Watermelon wedge with mint leaves"></div>
    <p class="flavor">WATERMELON<br>MINT</p>
    <div class="claims">
      <div class="claim">
        <div class="claim__icon">
          <svg width="22" height="22" viewBox="0 0 24 24" aria-hidden="true"><path d="M12 20 C12 14 9 10 4 9 C4 15 7 19 12 20 Z M12 20 C12 14 15 10 20 9 C20 15 17 19 12 20 Z" fill="var(--ink)"/></svg>
        </div>
        <p class="claim__text">Plant<br>Based</p>
      </div>
      <div class="claim">
        <div class="claim__icon">
          <svg width="20" height="22" viewBox="0 0 20 24" aria-hidden="true"><path d="M10 2 C6 9 4 12 4 15.5 A6 6 0 0 0 16 15.5 C16 12 14 9 10 2 Z" fill="var(--ink)"/></svg>
        </div>
        <p class="claim__text">Low<br>Sugar</p>
      </div>
      <div class="claim">
        <div class="claim__icon">
          <svg width="22" height="22" viewBox="0 0 24 24" aria-hidden="true"><path d="M12 21 V6 M12 14 C9 12 8 9 8 6 M12 14 C15 12 16 9 16 6" stroke="var(--ink)" stroke-width="1.8" fill="none" stroke-linecap="round"/></svg>
        </div>
        <p class="claim__text">Made with<br>real sea moss</p>
      </div>
    </div>
    <p class="volume">12 FL OZ (355 mL)</p>
    <div class="can__rim can__rim--bottom"></div>
  </section>

</main>
</body>
</html>
```